Business card for law firm

Need business card for new law firm. Think confident, authoritative, conservative, but not stuffy or old-fashioned.

Contact Information for Business Card

Content for card - logo (uploaded), plus the following:

Paul Wexbury (larger font)
Managing Partner (larger font, but not as large as name)
Level 9, 41 Tansy Lane
Sydney NSW 2000
Main Tel 02 7346 2190
Direct Tel 02 6273 4415
Email paul@qvlegal.com.au
www.qvlegal.com.au

Letterhead design should include logo plus:
Level 9, 41 Tansy Lane
Sydney NSW 2000
Tel 02 6273 4415
www.qvlegal.com.au

```html
<!DOCTYPE html>
<html lang="en">
<head>
<meta charset="utf-8">
<title>Quayvale Lawyers – Business Card</title>
<link href="https://fonts.googleapis.com/css2?family=Cinzel:wght@700&family=Raleway:wght@400;500&display=swap" rel="stylesheet">
<style>
  :root {
    --navy: #1d2660;
    --navy-deep: #151c4a;
    --ink: #111111;
    --paper: #ffffff;
    --paper-shade: #e4e5e8;
    --silver: #d7dae2;
    --backdrop: #3a3b3f;
  }
  * { margin: 0; padding: 0; box-sizing: border-box; }
  html, body { width: 1200px; height: 900px; overflow: hidden; }
  body {
    background: var(--backdrop);
    position: relative;
    font-family: 'Raleway', sans-serif;
  }
  .card {
    position: absolute;
    left: 285px;
    width: 630px;
    height: 360px;
    border-radius: 18px;
    overflow: hidden;
  }
  .card--front {
    top: 60px;
    background: linear-gradient(160deg, var(--paper) 45%, var(--paper-shade) 100%);
  }
  .card--back {
    top: 480px;
    background: radial-gradient(ellipse at 40% 35%, var(--navy) 0%, var(--navy-deep) 100%);
  }

  .brand {
    position: absolute;
    display: flex;
    align-items: center;
    gap: 12px;
    font-family: 'Raleway', sans-serif;
    font-weight: 500;
    white-space: nowrap;
  }
  .brand__mark { flex: none; }

  .card--front .brand {
    top: 44px; left: 0; width: 100%; justify-content: center;
    color: var(--ink); font-size: 34px;
  }
  .card--front .brand__mark { width: 18px; height: 18px; background: var(--ink); }

  .address {
    position: absolute; top: 138px; left: 40px;
    color: var(--navy); font-size: 15px; line-height: 1.35; font-weight: 500;
  }
  .contacts {
    position: absolute; top: 196px; left: 40px;
    color: var(--navy); font-size: 15px; line-height: 1.5; font-weight: 500;
    list-style: none;
  }
  .contacts li { display: flex; align-items: center; gap: 9px; }
  .contacts li.email { font-size: 13px; font-weight: 400; }
  .contacts svg { width: 11px; height: 11px; flex: none; }

  .rule {
    position: absolute; left: 40px; right: 40px; top: 296px;
    height: 1.5px; background: var(--navy);
  }

  .person {
    position: absolute; right: 40px; top: 236px; text-align: right; color: var(--navy);
  }
  .person__name { font-family: 'Cinzel', serif; font-weight: 700; font-size: 24px; letter-spacing: 0.5px; line-height: 1; }
  .person__title { font-size: 16px; font-weight: 500; margin-top: 6px; }

  .swoosh { position: absolute; left: 0; bottom: 0; width: 630px; height: 70px; }

  .card--back .brand {
    top: 128px; left: 0; width: 100%; justify-content: center;
    color: var(--silver); font-size: 42px;
  }
  .card--back .brand__mark { width: 22px; height: 22px; background: var(--silver); }
  .website {
    position: absolute; top: 238px; width: 100%; text-align: center;
    color: var(--silver); font-size: 17px; letter-spacing: 4px;
  }
</style>
</head>
<body>

<section class="card card--front">
  <div class="brand">
    <span class="brand__mark" aria-hidden="true"></span>
    <span class="brand__name">Quayvale Lawyers</span>
  </div>

  <p class="address">Level 9, 41 Tansy Lane<br>Sydney NSW 2000</p>

  <ul class="contacts">
    <li>
      <svg viewBox="0 0 12 12" aria-hidden="true"><path d="M2.5 1 L4.5 1 L5.2 3.5 L4 4.5 Q5 7 7.5 8 L8.5 6.8 L11 7.5 L11 9.5 Q10.5 11 9 11 Q1 10 1 2.5 Q1 1 2.5 1 Z" fill="var(--navy)"/></svg>
      02 7346 2190
    </li>
    <li>
      <svg viewBox="0 0 12 12" aria-hidden="true"><rect x="3" y="0.8" width="6.5" height="10.4" rx="1.2" fill="none" stroke="var(--navy)" stroke-width="1.3"/><circle cx="6.25" cy="9.2" r="0.7" fill="var(--navy)"/></svg>
      02 6273 4415
    </li>
    <li class="email">
      <svg viewBox="0 0 12 12" aria-hidden="true"><rect x="0.8" y="2.2" width="10.4" height="7.6" rx="0.8" fill="none" stroke="var(--navy)" stroke-width="1.2"/><path d="M1 2.6 L6 6.6 L11 2.6" fill="none" stroke="var(--navy)" stroke-width="1.2"/></svg>
      paul@qvlegal.com.au
    </li>
  </ul>

  <div class="person">
    <div class="person__name">PAUL WEXBURY</div>
    <div class="person__title">Managing Partner</div>
  </div>
  <div class="rule"></div>

  <svg class="swoosh" viewBox="0 0 630 70" preserveAspectRatio="none" aria-hidden="true">
    <path d="M0 8 Q140 10 250 70 L0 70 Z" fill="var(--navy)"/>
    <path d="M0 0 Q170 2 300 70 L250 70 Q140 12 0 12 Z" fill="var(--ink)"/>
  </svg>
</section>

<section class="card card--back">
  <div class="brand">
    <span class="brand__mark" aria-hidden="true"></span>
    <span class="brand__name">Quayvale Lawyers</span>
  </div>
  <p class="website">www.qvlegal.com.au</p>
</section>

</body>
</html>
```